Clearbrook Waterworks LLC Business Card

Ok, first off let me thank you for taking the time to participate in this project !! I have my business logo that I want incorporated into business card design . My irrigation business is located in a very upscale part of town and we do high end homes . So with that said I'm planning on these cards being plastic credit card type cards. I would like them to be two sided . I'm thinking something bold , yet classy and clean . Not too busy . We do different types of work . 80% irrigation service and installation . 15% landscape lighting and the other 5% drainage and hardscapes ! I have a website that I want listed on it as well as our address , phone number and of course my name and title .
Updates

Target Market(s)

Upscale homeowners and architects

Industry/Entity Type

Landscape

Requirements
Must have
• Company logo, website, address , phone number , name , title , services offered

Www.ClearbrookWaterworks.example
Marcus Hale owner
205-418-7752
Clearbrook Waterworks LLC
P.O. Box 947215
Birmingham, Alabama 35094

```html
<!DOCTYPE html>
<html lang="en">
<head>
<meta charset="utf-8">
<title>Clearbrook Waterworks LLC – Business Cards</title>
<link href="https://fonts.googleapis.com/css2?family=Nunito+Sans:wght@400;600;800&display=swap" rel="stylesheet">
<style>
  :root {
    --stage: #dcdfe0;
    --card-light: #ffffff;
    --card-dark: #000000;
    --brand-blue: #2f8fd8;
    --brand-sky: #3aa8e8;
    --brand-green: #7fd321;
    --owner-green: #7cc61e;
    --ink: #1c1c1c;
    --ink-light: #f2f2f2;
    --name-blue-dark: #56c4ee;
    --divider: #555555;
  }
  * { box-sizing: border-box; margin: 0; padding: 0; }
  html, body { width: 1200px; height: 694px; overflow: hidden; }
  body {
    background: var(--stage);
    font-family: "Nunito Sans", sans-serif;
    position: relative;
  }
  .card {
    position: absolute;
    width: 510px;
    height: 292px;
    border-radius: 30px;
    overflow: hidden;
    box-shadow: 0 4px 12px rgba(0,0,0,0.25);
  }
  .card--light { background: var(--card-light); color: var(--ink); }
  .card--dark { background: var(--card-dark); color: var(--ink-light); }
  .card--front-light { left: 48px; top: 30px; }
  .card--back-light { left: 641px; top: 44px; }
  .card--front-dark { left: 48px; top: 362px; }
  .card--back-dark { left: 641px; top: 375px; }

  .brand { position: absolute; text-align: center; }
  .brand__dot {
    display: block;
    margin: 0 auto;
    border-radius: 50%;
    background: var(--brand-blue);
  }
  .brand__name {
    display: block;
    font-weight: 800;
    color: var(--brand-green);
    white-space: nowrap;
    letter-spacing: -0.3px;
  }
  .card--front-light .brand, .card--front-dark .brand { left: 10px; width: 300px; top: 60px; }
  .card--front-light .brand__dot, .card--front-dark .brand__dot { width: 88px; height: 88px; }
  .card--front-light .brand__name, .card--front-dark .brand__name { font-size: 25px; margin-top: 10px; }
  .card--back-light .brand, .card--back-dark .brand { left: 0; width: 510px; top: 30px; }
  .card--back-light .brand__dot, .card--back-dark .brand__dot { width: 112px; height: 112px; }
  .card--back-light .brand__name, .card--back-dark .brand__name { font-size: 34px; margin-top: 18px; }

  .divider {
    position: absolute;
    left: 335px; top: 76px;
    width: 1px; height: 142px;
    background: var(--divider);
  }
  .contact { position: absolute; left: 348px; top: 74px; }
  .contact__name { font-size: 16px; font-weight: 600; color: var(--brand-blue); line-height: 20px; }
  .card--dark .contact__name { color: var(--name-blue-dark); }
  .contact__title { font-size: 16px; font-weight: 600; color: var(--owner-green); line-height: 20px; margin-bottom: 8px; }
  .contact__line { font-size: 12px; line-height: 20.5px; white-space: nowrap; }
  .contact__phone { display: flex; align-items: center; gap: 4px; }
  .contact__phone svg { width: 12px; height: 12px; }

  .band {
    position: absolute;
    left: 0; bottom: 0;
    width: 285px; height: 20px;
    background: var(--brand-green);
    clip-path: polygon(0 0, 100% 0, 94% 100%, 0 100%);
  }
  .web-tab {
    position: absolute;
    right: 0; bottom: 0;
    width: 252px; height: 27px;
    background: var(--brand-sky);
    clip-path: polygon(10% 0, 100% 0, 100% 100%, 0 100%);
    color: #ffffff;
    font-size: 12px;
    font-weight: 600;
    line-height: 27px;
    padding-left: 30px;
    white-space: nowrap;
  }
</style>
</head>
<body>

  <section class="card card--light card--front-light" aria-label="Front of card, light">
    <div class="brand">
      <span class="brand__dot"></span>
      <span class="brand__name">Clearbrook Waterworks</span>
    </div>
    <div class="divider"></div>
    <div class="contact">
      <p class="contact__name">Marcus Hale</p>
      <p class="contact__title">owner</p>
      <p class="contact__line">Clearbrook Waterworks LLC</p>
      <p class="contact__line">P.O. Box 947215</p>
      <p class="contact__line">Birmingham,</p>
      <p class="contact__line">Alabama 35094</p>
      <p class="contact__line contact__phone">
        <svg viewBox="0 0 24 24" aria-hidden="true"><path fill="var(--brand-blue)" d="M6.6 10.8a15 15 0 0 0 6.6 6.6l2.2-2.2a1 1 0 0 1 1-.25 11.4 11.4 0 0 0 3.6.57 1 1 0 0 1 1 1V20a1 1 0 0 1-1 1A17 17 0 0 1 3 4a1 1 0 0 1 1-1h3.5a1 1 0 0 1 1 1c0 1.25.2 2.45.57 3.6a1 1 0 0 1-.25 1z"/></svg>
        205-418-7752
      </p>
    </div>
    <div class="band"></div>
    <div class="web-tab">Www.ClearbrookWaterworks.example</div>
  </section>

  <section class="card card--light card--back-light" aria-label="Back of card, light">
    <div class="brand">
      <span class="brand__dot"></span>
      <span class="brand__name">Clearbrook Waterworks</span>
    </div>
    <div class="band"></div>
    <div class="web-tab">Www.ClearbrookWaterworks.example</div>
  </section>

  <section class="card card--dark card--front-dark" aria-label="Front of card, dark">
    <div class="brand">
      <span class="brand__dot"></span>
      <span class="brand__name">Clearbrook Waterworks</span>
    </div>
    <div class="divider"></div>
    <div class="contact">
      <p class="contact__name">Marcus Hale</p>
      <p class="contact__title">owner</p>
      <p class="contact__line">Clearbrook Waterworks LLC</p>
      <p class="contact__line">P.O. Box 947215</p>
      <p class="contact__line">Birmingham,</p>
      <p class="contact__line">Alabama 35094</p>
      <p class="contact__line contact__phone">
        <svg viewBox="0 0 24 24" aria-hidden="true"><path fill="var(--name-blue-dark)" d="M6.6 10.8a15 15 0 0 0 6.6 6.6l2.2-2.2a1 1 0 0 1 1-.25 11.4 11.4 0 0 0 3.6.57 1 1 0 0 1 1 1V20a1 1 0 0 1-1 1A17 17 0 0 1 3 4a1 1 0 0 1 1-1h3.5a1 1 0 0 1 1 1c0 1.25.2 2.45.57 3.6a1 1 0 0 1-.25 1z"/></svg>
        205-418-7752
      </p>
    </div>
    <div class="band"></div>
    <div class="web-tab">Www.ClearbrookWaterworks.example</div>
  </section>

  <section class="card card--dark card--back-dark" aria-label="Back of card, dark">
    <div class="brand">
      <span class="brand__dot"></span>
      <span class="brand__name">Clearbrook Waterworks</span>
    </div>
    <div class="band"></div>
    <div class="web-tab">Www.ClearbrookWaterworks.example</div>
  </section>

</body>
</html>
```